redesign my website bluekelpvoyages.com and make it user friendly

I already have a website, bluekelpvoyages.com, and want a redesign in WordPress with Elementor Pro, using the same text/content. The goal is to improve:

Design quality (colors, fonts, spacing, visual flow)
User experience (easy navigation, clear offers)
Conversion readiness (calls-to-action, trust signals, booking flow)
Technical side (SEO basics, fast speed, full mobile responsiveness)

The site should look modern, clean, fun, engaging, interactive and optimized for speed and usability.

I would like the 11 page to be consolidate dto 6 as follows: Home (main landing, highlights)

Sailboat Trips (all packages, itineraries, pricing)
Boats (fleet details, features, photos)
How It Works (booking process, FAQs, travel info, what to expect)
Blog
Contact Us (form, WhatsApp, phone, etc.)

Target Market(s)

sailboat trip customers for Coral Mira Keys in Panama

Industry/Entity Type

Travel, Boat Tour Agency

Coding

Number of Pages Required

3 page

Font styles to use
Sans Serif
Other font styles liked:
• Oswalg and sans serif

Colors
0054AA
0677BA
7BADD7
CADEEF
E8F1F8
0094D4
00A9DD
6FCCEA
C7EBF8
E9F6FB
FFC000
F8CF3A
FAE287
FDF2CF
FEFAEE
F0912C
F2A743
F7CA91
FBE8D2
FDF5EE

Requirements
Must have
• Home (main landing, highlights) Sailboat Trips (all packages, itineraries, pricing) Boats (fleet details, features, photos) How It Works (booking process, FAQs, travel info, what to expect) Blog (updates, travel tips, inspiration) Contact Us (form, WhatsApp, phone, etc.)
Nice to have
• I want it to look professionla and be very user friendy to entice people to contact me to book boat trips
Should not have
• a store

```html
<!DOCTYPE html>
<html lang="en">
<head>
<meta charset="utf-8">
<title>Blue Kelp Voyages — Coral Mira Keys Sailing</title>
<link href="https://fonts.googleapis.com/css2?family=Oswald:wght@400;500;600;700&family=Open+Sans:wght@400;600;700&display=swap" rel="stylesheet">
<style>
:root{
  --navy:#0054AA; --blue:#0677BA; --sky:#7BADD7; --mist:#CADEEF; --ice:#E8F1F8;
  --cyan:#0094D4; --aqua:#00A9DD; --lagoon:#6FCCEA; --foam:#C7EBF8;
  --orange:#F0912C; --orange-lt:#F2A743; --sand:#FBE8D2;
  --ink:#1d2433; --muted:#5a6475; --dark:#0d0f13; --white:#fff;
}
*{box-sizing:border-box;margin:0;padding:0}
html,body{width:1200px;height:4536px;overflow:hidden}
body{font-family:"Open Sans",Arial,sans-serif;color:var(--ink);background:#fff;position:relative}
.abs{position:absolute}
h1,h2,h3,h4,.osw{font-family:"Oswald","Arial Narrow",sans-serif}
.accent{color:var(--orange)}
.btn{display:inline-block;background:var(--orange);color:#fff;font-family:"Oswald",sans-serif;font-weight:500;font-size:14px;letter-spacing:.5px;text-transform:uppercase;padding:12px 26px;border-radius:4px}

/* header */
.topbar{left:0;top:0;width:1200px;height:92px;background:#fff}
.brand{left:70px;top:24px;display:flex;align-items:center;gap:12px}
.brand-dot{width:40px;height:40px;border-radius:50%;background:var(--navy)}
.brand-name{font-family:"Oswald",sans-serif;font-weight:600;font-size:24px;color:var(--navy)}
.call{left:820px;top:24px;display:flex;align-items:center;gap:10px}
.call-ico{width:40px;height:40px;border-radius:50%;border:2px solid var(--orange);display:flex;align-items:center;justify-content:center}
.call small{display:block;font-size:11px;color:var(--muted)}
.call strong{font-family:"Oswald",sans-serif;font-size:20px;color:var(--orange)}
.top-cta{left:990px;top:24px}
.nav{left:0;top:92px;width:1200px;height:48px;background:linear-gradient(90deg,var(--navy),var(--blue));display:flex;align-items:center;padding-left:80px}
.nav a{color:#fff;font-size:14px;font-weight:600;padding:14px 18px;text-decoration:none}
.nav a.active{background:rgba(255,255,255,.18)}

/* hero */
.hero{left:0;top:140px;width:1200px;height:640px;background:linear-gradient(180deg,#7fb7d8 0%,#4aa6cf 30%,#1fb3c7 58%,#0f8fb0 100%)}
.hero-copy{left:0;top:195px;width:1200px;text-align:center;color:#fff;text-shadow:0 2px 6px rgba(0,0,0,.3)}
.hero-copy h1{font-size:62px;font-weight:700;line-height:1.05}
.hero-copy p{font-family:"Oswald",sans-serif;font-size:28px;font-weight:500;line-height:1.2;margin-top:8px}
.hero-copy .btn{margin-top:26px;text-shadow:none}
.hero-wave{left:0;top:640px}

/* discover */
.sec-title{left:0;width:1200px;text-align:center;font-size:44px;font-weight:700;color:var(--ink)}
.card{width:260px;height:310px;border:3px solid var(--navy);border-radius:6px;background:#fff;text-align:center;padding:80px 22px 0}
.card-ico{position:absolute;left:50%;top:-26px;margin-left:-40px;width:80px;height:80px;background:#fff;display:flex;align-items:center;justify-content:center}
.card h3{font-size:20px;font-weight:600;color:var(--ink);border-bottom:1px solid var(--mist);padding-bottom:12px;margin-bottom:12px}
.card p{font-size:12px;line-height:1.6;color:var(--muted)}

/* fleet */
.boat{width:272px;height:500px;background:#fff;border-radius:6px;box-shadow:0 4px 14px rgba(0,40,90,.15);overflow:hidden;text-align:center}
.boat-img{height:170px;background:linear-gradient(160deg,#5fc6dd,#178fb2 60%,#0d6f95)}
.boat-body{padding:14px 16px}
.boat-type{font-size:11px;font-weight:700;color:var(--orange);letter-spacing:1px}
.boat h3{font-size:26px;color:var(--navy);font-weight:600}
.boat .tag{font-size:12px;color:var(--muted);margin-bottom:8px}
.boat .quote{font-size:11.5px;line-height:1.55;color:var(--muted);min-height:120px}
.specs{display:flex;justify-content:space-around;border-top:1px solid var(--mist);border-bottom:1px solid var(--mist);padding:8px 0;font-size:11px;font-weight:600;color:var(--ink);margin:10px 0 14px}
.boat .btn{font-size:12px;padding:9px 22px}
.arrow{width:46px;height:46px;border-radius:50%;background:var(--navy);display:flex;align-items:center;justify-content:center}

/* testimonials */
.testi-panel{left:180px;top:2330px;width:1020px;height:660px;background:linear-gradient(135deg,var(--navy),var(--blue))}
.testi-photo{left:32px;top:2520px;width:390px;height:360px;border:8px solid #fff;background:linear-gradient(180deg,#8ec9e8,#3f9cc6 55%,#1c6f98);box-shadow:0 6px 18px rgba(0,0,0,.25)}
.testi-copy{left:470px;top:2370px;width:640px;color:#fff}
.testi-copy h2{font-size:44px;font-weight:600;margin-bottom:20px}
.testi-copy p{font-size:14px;line-height:1.75;margin-bottom:18px;color:#e8f1f8}
.testi-copy h4{font-size:22px;font-weight:500}
.stars{color:var(--orange-lt);font-size:22px;letter-spacing:3px}
.dots{left:1020px;top:2920px;display:flex;gap:8px}
.dots span{width:26px;height:26px;border-radius:50%;background:var(--orange)}

/* form */
.form-bg{left:600px;top:3200px;width:600px;height:740px;background:radial-gradient(ellipse at 60% 50%,rgba(123,173,215,.35),rgba(232,241,248,.2) 55%,rgba(255,255,255,0) 75%)}
.form{left:270px;top:3240px;width:660px}
.field{height:46px;border:1px solid #cfd6df;background:#fff;border-radius:3px;display:flex;align-items:center;gap:10px;padding:0 14px;font-size:14px;color:var(--muted);margin-bottom:14px}
.field .dot{width:14px;height:14px;border-radius:3px;background:var(--orange)}
.row{display:flex;gap:14px}
.row .field{flex:1}
.radio{display:flex;gap:36px;font-size:14px;margin:4px 0 16px}
.radio span::before,.checks span::before{content:"";display:inline-block;width:13px;height:13px;border:1px solid #9aa3b0;border-radius:50%;margin-right:8px;vertical-align:-2px}
.checks-q{font-size:14px;font-weight:600;margin:6px 0 10px}
.checks{display:grid;grid-template-columns:repeat(3,1fr);row-gap:10px;font-size:13px;color:var(--muted);margin-bottom:18px}
.checks span::before{border-radius:2px}
.textarea{height:150px;align-items:flex-start;padding-top:14px}
.send{left:0;top:3868px;width:1200px;text-align:center}

/* footer */
.footer{left:0;top:4040px;width:1200px;height:496px;background:var(--dark);color:#c9ced6}
.f-brand{left:110px;top:4205px;display:flex;align-items:center;gap:12px}
.f-brand .brand-dot{background:var(--aqua)}
.f-brand .brand-name{color:#fff}
.socials{left:160px;top:4275px;display:flex;gap:12px}
.socials span{width:30px;height:30px;border-radius:50%;background:#3a3f48}
.socials span.on{background:var(--orange)}
.f-col{color:#c9ced6}
.f-col h4{color:#fff;font-size:20px;font-weight:600;margin-bottom:14px}
.f-col a{display:block;color:#c9ced6;font-size:13px;line-height:2;text-decoration:none}
.f-contact li{list-style:none;display:flex;gap:12px;margin-bottom:14px;font-size:13px;line-height:1.4;color:#c9ced6}
.f-contact .ic{width:30px;height:30px;border-radius:50%;background:var(--orange);flex:none;display:flex;align-items:center;justify-content:center}
.f-contact small{display:block;color:#8a919c;font-size:11px}
.copy{left:0;top:4488px;width:1200px;border-top:1px solid #2a2e35;padding-top:14px;text-align:center;font-size:12px;color:#8a919c}
</style>
</head>
<body>

<header>
  <div class="abs topbar"></div>
  <div class="abs brand"><span class="brand-dot"></span><span class="brand-name">Blue Kelp Voyages</span></div>
  <div class="abs call">
    <span class="call-ico"><svg width="18" height="18" viewBox="0 0 24 24" fill="none" stroke="#F0912C" stroke-width="2"><path d="M22 16.9v3a2 2 0 0 1-2.2 2 19.8 19.8 0 0 1-8.6-3.1 19.5 19.5 0 0 1-6-6A19.8 19.8 0 0 1 2.1 4.2 2 2 0 0 1 4.1 2h3a2 2 0 0 1 2 1.7c.1 1 .4 1.9.7 2.8a2 2 0 0 1-.5 2.1L8 9.9a16 16 0 0 0 6 6l1.3-1.3a2 2 0 0 1 2.1-.4c.9.3 1.8.6 2.8.7a2 2 0 0 1 1.7 2z"/></svg></span>
    <div><small>Call Anytime</small><strong>555.014.2290</strong></div>
  </div>
  <a class="abs btn top-cta">Contact Us</a>
  <nav class="abs nav">
    <a class="active">Blue Kelp Voyages</a><a>Guna Yala</a><a>Fleet</a><a>About Us</a><a>Book Now</a><a>Pricing</a><a>Itineraries</a><a>Activities</a><a>Blog</a><a>FAQs</a>
  </nav>
</header>

<section class="abs hero" role="img" aria-label="Aerial photo of a catamaran anchored beside a palm-covered island in turquoise Caribbean water"></section>
<div class="abs hero-copy">
  <h1>CORAL MIRA KEYS:</h1>
  <p>PANAMA SAILING VACATIONS,<br>ULTIMATE BEACHES &amp; CATAMARAN TOURS</p>
  <a class="btn">Charter Inquiry Form</a>
</div>
<svg class="abs hero-wave" width="1200" height="140" viewBox="0 0 1200 140">
  <path d="M0 60 Q600 150 1200 40 L1200 140 L0 140Z" fill="#F0912C"/>
  <path d="M0 78 Q600 165 1200 58 L1200 140 L0 140Z" fill="#0054AA"/>
  <path d="M0 92 Q600 178 1200 74 L1200 140 L0 140Z" fill="#fff"/>
</svg>

<h2 class="abs sec-title" style="top:845px">DISCOVER ULTIMATE <span class="accent">PANAMA SAILING TOURS</span></h2>

<div class="abs card" style="left:108px;top:970px">
  <div class="card-ico"><svg width="44" height="44" viewBox="0 0 24 24" fill="none" stroke="#0054AA" stroke-width="2"><circle cx="12" cy="5" r="2"/><path d="M12 7v14M5 12H2a10 10 0 0 0 20 0h-3M8 10h8"/></svg></div>
  <h3>PRIVATE CHARTERS</h3>
  <p>Sail the beautiful islands and beaches of Coral Mira Keys on a private all-inclusive catamaran. Enjoy a custom itinerary, friendly crew, and flexible options to fit any budget, perfect for a relaxing escape.</p>
</div>
<div class="abs card" style="left:470px;top:970px">
  <div class="card-ico"><svg width="44" height="44" viewBox="0 0 24 24" fill="none" stroke="#0054AA" stroke-width="2"><circle cx="8" cy="7" r="3"/><circle cx="16" cy="7" r="3"/><path d="M2 20a6 6 0 0 1 12 0M10 20a6 6 0 0 1 12 0"/></svg></div>
  <h3>SHARED CHARTERS</h3>
  <p>Share the experience with others for a more affordable alternative to a private charter. Perfect for couples, solo travelers and small groups: enjoy island beaches, clear waters, great meals and a relaxed atmosphere with a welcoming crew.</p>
</div>
<div class="abs card" style="left:832px;top:970px">
  <div class="card-ico"><svg width="44" height="44" viewBox="0 0 24 24" fill="none" stroke="#0054AA" stroke-width="2"><circle cx="7" cy="6" r="2.5"/><circle cx="17" cy="6" r="2.5"/><circle cx="12" cy="11" r="2"/><path d="M3 21v-6a4 4 0 0 1 8 0M13 15a4 4 0 0 1 8 0v6M9 21v-3a3 3 0 0 1 6 0v3"/></svg></div>
  <h3>FAMILY FRIENDLY BOAT TRIPS</h3>
  <p>Coral Mira Keys is perfect for kids, with calm waters, safe snorkeling, and fun island hopping. Families love the mix of adventure and culture, an ideal way to explore Panama together.</p>
</div>
<div class="abs" style="left:0;top:1310px;width:1200px;text-align:center"><a class="btn">Request a Quote</a></div>

<svg class="abs" style="left:0;top:1400px" width="1200" height="40" viewBox="0 0 1200 40">
  <path d="M0 10 Q600 40 1200 10 L1200 22 Q600 52 0 22Z" fill="#CADEEF"/>
</svg>

<h2 class="abs sec-title" style="top:1530px">FEATURED <span class="accent">CATAMARANS</span></h2>

<div class="abs boat" style="left:-200px;top:1680px"><div class="boat-img" role="img" aria-label="Catamaran at anchor in clear water"></div>
  <div class="boat-body"><div class="boat-type">CATAMARAN</div><h3>MARISOL 42</h3><p class="tag">Service that exceeds all expectations!</p><p class="quote">"We started as strangers and left as friends! The crew made sure everyone felt welcome, and every moment was filled with fun and laughter."</p><div class="specs"><span>42FT</span><span>3 CABIN</span><span>8 GUEST</span></div><a class="btn">Info &amp; Price</a></div></div>

<div class="abs boat" style="left:168px;top:1680px"><div class="boat-img" role="img" aria-label="Catamaran sailing near a small island"></div>
  <div class="boat-body"><div class="boat-type">CATAMARAN</div><h3>MARISOL 42</h3><p class="tag">Service that exceeds all expectations!</p><p class="quote">"We started as strangers and left as friends! The crew made sure everyone felt welcome, and every moment was filled with fun and laughter."</p><div class="specs"><span>42FT</span><span>3 CABIN</span><span>8 GUEST</span></div><a class="btn">Info &amp; Price</a></div></div>

<div class="abs boat" style="left:464px;top:1680px"><div class="boat-img" role="img" aria-label="Catamaran deck with guests relaxing"></div>
  <div class="boat-body"><div class="boat-type">CATAMARAN</div><h3>MARISOL 42</h3><p class="tag">Service that exceeds all expectations!</p><p class="quote">"We started as strangers and left as friends! The crew made sure everyone felt welcome, and every moment was filled with fun and laughter."</p><div class="specs"><span>42FT</span><span>3 CABIN</span><span>8 GUEST</span></div><a class="btn">Info &amp; Price</a></div></div>

<div class="abs boat" style="left:760px;top:1680px"><div class="boat-img" role="img" aria-label="Aerial view of a catamaran over a reef"></div>
  <div class="boat-body"><div class="boat-type">CATAMARAN</div><h3>MARISOL 42</h3><p class="tag">Service that exceeds all expectations!</p><p class="quote">"We started as strangers and left as friends! The crew made sure everyone felt welcome, and every moment was filled with fun and laughter."</p><div class="specs"><span>42FT</span><span>3 CABIN</span><span>8 GUEST</span></div><a class="btn">Info &amp; Price</a></div></div>

<div class="abs boat" style="left:1056px;top:1680px"><div class="boat-img" role="img" aria-label="Catamaran moored off a sandy beach"></div>
  <div class="boat-body"><div class="boat-type">CATAMARAN</div><h3>MARISOL 42</h3><p class="tag">Service that exceeds all expectations!</p><p class="quote">"We started as strangers and left as friends! The crew made sure everyone felt welcome, and every moment was filled with fun and laughter."</p><div class="specs"><span>42FT</span><span>3 CABIN</span><span>8 GUEST</span></div><a class="btn">Info &amp; Price</a></div></div>

<div class="abs arrow" style="left:128px;top:1800px"><svg width="18" height="18" viewBox="0 0 24 24" fill="none" stroke="#fff" stroke-width="3"><path d="M15 5l-7 7 7 7"/></svg></div>
<div class="abs arrow" style="left:1026px;top:1800px"><svg width="18" height="18" viewBox="0 0 24 24" fill="none" stroke="#fff" stroke-width="3"><path d="M9 5l7 7-7 7"/></svg></div>

<section class="abs testi-panel"></section>
<div class="abs testi-photo" role="img" aria-label="Guests swimming beside their catamaran in the sea"></div>
<div class="abs testi-copy">
  <h2>TESTIMONIALS</h2>
  <p>My wife and I booked from the UK to visit Coral Mira Keys. Our 3 night 3 day trip on a catamaran was a once in a lifetime experience. It started with a smooth transfer from our hotel in Panama to the boat at the Keys, followed by exceptional hospitality by Tomas and Lena throughout our stay. Catering for our every need. The beauty of the islands was everything we hoped for. We were taken to different islands each with unique features, met the island people and learned about their culture, we kayaked, snorkeled and ate great food throughout the stay prepared by Lena. And of course enjoyed the amazing beaches. I cannot recommend this experience enough.</p>
  <p>The transport back to Panama city was also a very smooth process.</p>
  <p>The owner was contactable and helpful to the build up and during the stay. A nice review from me, I couldn't recommend this experience enough!</p>
  <h4>Daniel R. Whitcombe</h4>
  <div class="stars">★★★★★</div>
</div>
<div class="abs dots"><span></span><span></span></div>

<h2 class="abs sec-title" style="top:3110px">CHARTER <span class="accent">INQUIRY FORM</span></h2>
<div class="abs form-bg" role="img" aria-label="Faint aerial view of islands and lagoon behind the form"></div>
<form class="abs form">
  <div class="field"><span class="dot"></span>Your Name *</div>
  <div class="field"><span class="dot"></span>Email *</div>
  <div class="field"><span class="dot"></span>Whatsapp Number *</div>
  <div class="radio"><span>Private Charter</span><span>Shared Charter</span></div>
  <div class="row">
    <div class="field"><span class="dot"></span>Number of Passengers</div>
    <div class="field"><span class="dot"></span>Number of Days</div>
    <div class="field"><span class="dot"></span>mm/dd/yyyy</div>
  </div>
  <p class="checks-q">What type of experience are you looking for? (Check all that apply)</p>
  <div class="checks">
    <span>Relaxing and disconnected</span><span>Island-hopping adventure</span><span>Snorkeling &amp; marine life</span>
    <span>Cultural exchange with locals</span><span>Family-friendly</span><span>Romantic getaway</span>
    <span>Food &amp; wine focused</span><span>Sailing focused</span><span>Luxury experience</span>
  </div>
  <div class="field textarea"><span class="dot"></span>Enter Your Message *</div>
</form>
<div class="abs send"><a class="btn">Send Message</a></div>

<footer class="abs footer"></footer>
<div class="abs f-brand"><span class="brand-dot"></span><span class="brand-name">Blue Kelp Voyages</span></div>
<div class="abs socials"><span></span><span class="on"></span><span></span></div>
<div class="abs f-col" style="left:460px;top:4160px">
  <h4>QUICK LINKS</h4>
  <a>Home</a><a>Blue Kelp Voyages</a><a>Guna Yala</a><a>Fleet</a><a>About Us</a><a>Book Now</a><a>FAQs</a>
</div>
<div class="abs f-col" style="left:640px;top:4160px">
  <h4>LINKS</h4>
  <a>Pricing</a><a>Itineraries</a><a>Activities</a><a>Blog</a><a>Privacy Policy</a><a>Accessibility</a><a>Contact Us</a>
</div>
<div class="abs f-col" style="left:800px;top:4160px">
  <h4>CONTACT US</h4>
  <ul class="f-contact">
    <li><span class="ic"><svg width="14" height="14" viewBox="0 0 24 24" fill="#fff"><path d="M12 2a7 7 0 0 0-7 7c0 5 7 13 7 13s7-8 7-13a7 7 0 0 0-7-7zm0 9.5A2.5 2.5 0 1 1 12 6.5a2.5 2.5 0 0 1 0 5z"/></svg></span><div><small>Address</small>42 Harbour Lane,<br>Toronto, Canada</div></li>
    <li><span class="ic"><svg width="14" height="14" viewBox="0 0 24 24" fill="none" stroke="#fff" stroke-width="2.5"><path d="M22 16.9v3a2 2 0 0 1-2.2 2A19.8 19.8 0 0 1 2.1 4.2 2 2 0 0 1 4.1 2h3a2 2 0 0 1 2 1.7l.7 2.8-1.8 3.4a16 16 0 0 0 6 6l3.4-1.8 2.8.7a2 2 0 0 1 1.8 2z"/></svg></span><div><small>Call us</small>+57 555 010 2244</div></li>
    <li><span class="ic"><svg width="14" height="14" viewBox="0 0 24 24" fill="none" stroke="#fff" stroke-width="2.5"><rect x="3" y="5" width="18" height="14" rx="2"/><path d="M3 7l9 6 9-6"/></svg></span><div><small>Email</small>hello@bluekelpvoyages.com</div></li>
  </ul>
</div>
<div class="abs copy">©2025. All rights reserved</div>

</body>
</html>
```